Webdesign für Kanal Vertrieb
Zielgruppe
Die lotte & brandt Media Marketing GmbH beschäftigt sich mit der Entwicklung, Vermarktung und dem Vertrieb von Medialeistungen aus den Bereichen Print, TV, Radio, Internet (Digital) und Events. Weiterhin erstellt das Unternehmen Kommunikation- und Marketingkonzepte sowie die komplette Realisierung von Events und TV-Produktionen. Im Weiteren werden auch branchenverwandten Anwendungen und Bereiche abgedeckt, die den Unternehmenszielen dienen. Das Unternehmen betreut, vermittelt und vermarktet im weiteren Prominente, Kunstler und Moderatoren.
Die Zielgruppe ist B2B
Unsere Seite ist aktuell nun 2 Jahre alt und wir benötigen ein frisches Re-Design
Das Design soll zum Style des Logos passen, es soll elegant und professionelle hervorgehoben werden.
Die jetzige Seite findet mal unter www.lotte-brandt.de
Aufgabenstellung
Das Design soll frisch und elegant wirken, sowie einen professionellen Eindruck für eine Media Agentur machen. Das ganze soll dann im Anschluss in Word Press integrier bar sein und auch dort gepflegt werden.

```html
<!DOCTYPE html>
<html lang="de">
<head>
<meta charset="utf-8">
<title>lotte &amp; brandt – Kanal Vertrieb</title>
<link rel="stylesheet" href="https://fonts.googleapis.com/css2?family=Nunito+Sans:wght@300;400;600;700&family=Kaushan+Script&display=swap">
<style>
:root{
  --ink:#1a1a1a;
  --text:#3a3a3a;
  --muted:#6b6b6b;
  --panel:#f1f1f1;
  --line:#e2e2e2;
  --white:#ffffff;
  --accent:#f2c400;
}
*{box-sizing:border-box;margin:0;padding:0}
html,body{width:1200px;height:2651px;overflow:hidden}
body{position:relative;background:var(--white);font-family:"Nunito Sans",sans-serif;color:var(--text)}
.abs{position:absolute}
.script{font-family:"Kaushan Script",cursive;color:var(--ink);font-weight:400}

/* header */
.brand{left:90px;top:50px;width:260px;height:70px}
.brand-name{font-size:38px;font-weight:300;color:var(--ink);letter-spacing:1px;line-height:44px}
.brand-sub{font-size:10px;letter-spacing:6px;text-transform:uppercase;color:var(--muted);margin-left:32px}
.contact-line{top:28px;font-size:11.5px;color:var(--text);display:flex;align-items:center;gap:8px}
.nav{top:76px;left:432px;display:flex;font-size:15px;color:var(--text)}
.nav a{position:absolute;white-space:nowrap;text-decoration:none;color:inherit;top:2px}
.btn{background:var(--ink);color:var(--white);border-radius:14px;display:flex;align-items:center;justify-content:center;font-size:13px;font-weight:600;text-decoration:none}

/* hero */
.hero{left:0;top:144px;width:1200px;height:389px;background:linear-gradient(100deg,#b9aa92 0%,#8d8577 35%,#4a4743 60%,#1f1f20 80%,#3a3836 100%)}
.badge{left:931px;top:430px;width:182px;height:82px;background:var(--white);border-radius:0 0 0 10px;padding:10px 16px}
.badge-label{font-size:9.5px;color:var(--text)}
.badge-name{font-size:20px;font-weight:600;color:var(--ink);margin-top:14px;text-align:center}

/* clients */
.client{top:571px;transform:translateX(-50%);font-size:19px;font-weight:700;color:#4a4a4a;display:flex;align-items:center;gap:8px;white-space:nowrap}
.client i{display:block;width:14px;height:14px;background:#4a4a4a;border-radius:50%}

/* about */
.about-panel{left:87px;top:798px;width:546px;height:516px;background:var(--panel);border-radius:20px 0 0 0}
.about-title{left:87px;top:866px;width:490px;text-align:center;font-size:24px}
.about-text{left:147px;top:941px;width:372px;text-align:center;font-size:13px;line-height:17.5px;color:var(--text)}
.about-text p{margin-bottom:17.5px}
.about-photo{left:579px;top:739px;width:534px;height:513px;border-radius:0 0 20px 0;background:linear-gradient(135deg,#e7e6e1 0%,#9ea3a4 40%,#3c4148 65%,#1d1f22 100%)}

/* services */
.section-title{left:0;width:1200px;text-align:center;font-size:24px}
.card{width:335px;height:277px;border-radius:0 0 20px 0;overflow:hidden;background:#222}
.card-photo{height:218px}
.card-label{height:59px;display:flex;align-items:center;justify-content:center;gap:8px;color:var(--white);font-size:15px;text-align:center;line-height:20px}

/* cta */
.cta{left:0;top:2118px;width:1200px;height:231px;background:var(--panel)}
.cta-title{left:140px;top:2182px;width:400px;text-align:center;font-size:24px}
.cta-text{left:90px;top:2253px;width:530px;text-align:center;font-size:13px;line-height:18px}

/* footer */
.foot-col{top:2422px}
.foot-col h4{font-size:14px;font-weight:700;color:var(--ink);margin-bottom:40px}
.foot-col li{list-style:none;font-size:13px;line-height:24.7px;color:var(--text)}
.made{left:864px;top:2600px;font-size:12.5px;color:var(--text);display:flex;align-items:center;gap:6px}
</style>
</head>
<body>

<header>
  <div class="abs brand">
    <div class="brand-name">lotte &amp; brandt</div>
    <div class="brand-sub">Kanal Vertrieb</div>
  </div>
  <div class="abs contact-line" style="left:785px">
    <svg width="18" height="18" viewBox="0 0 24 24" fill="none" stroke="#555" stroke-width="1.4"><path d="M5 3h4l2 5-3 2a11 11 0 0 0 6 6l2-3 5 2v4a2 2 0 0 1-2 2A17 17 0 0 1 3 5a2 2 0 0 1 2-2z"/></svg>
    +49 (0) 211 - 44 55 66 70
  </div>
  <div class="abs contact-line" style="left:972px">
    <svg width="20" height="14" viewBox="0 0 20 14" fill="none" stroke="#555" stroke-width="1.2"><rect x="0.6" y="0.6" width="18.8" height="12.8"/><path d="M1 1l9 7 9-7"/></svg>
    hallo@lotte-brandt.de
  </div>
  <nav class="abs nav">
    <a style="left:0">Startseite</a>
    <a style="left:119px">Agentur</a>
    <a style="left:237px">Projekte</a>
    <a style="left:333px">Kompetenzen</a>
    <a style="left:473px">Karriere</a>
  </nav>
  <a class="abs btn" style="left:989px;top:76px;width:124px;height:26px">Kontakt</a>
</header>

<section>
  <div class="abs hero" role="img" aria-label="Fernsehdreh im Freien: Interview mit einem Koch vor einer Profikamera"></div>
  <div class="abs badge">
    <div class="badge-label">Wir sind exclusiver Parten von:</div>
    <div class="badge-name">Ferienblick</div>
  </div>
</section>

<section>
  <div class="abs client" style="left:187px">Kachelhaus<i></i></div>
  <div class="abs client" style="left:325px"><i></i>Aerolinie</div>
  <div class="abs client" style="left:463px">Mertens</div>
  <div class="abs client" style="left:600px"><i style="border-radius:0"></i>Kantwerk</div>
  <div class="abs client" style="left:738px">Fruchtgold</div>
  <div class="abs client" style="left:875px">Hoffmann</div>
  <div class="abs client" style="left:1014px">Brotzeitkiste</div>
  <svg class="abs" style="left:583px;top:635px" width="34" height="34" viewBox="0 0 34 34"><circle cx="17" cy="17" r="16.5" fill="var(--ink)"/><path d="M17 9v15M11 18l6 6 6-6" stroke="#fff" stroke-width="1.8" fill="none"/></svg>
</section>

<section>
  <div class="abs about-panel"></div>
  <h2 class="abs script about-title">Agentur für Kommunikation</h2>
  <div class="abs about-text">
    <p>Hey! Wir von der Lotte &amp; Brandt haben das Ziel als Ihre Full-Service Werbeagentur stets dafür zu sorgen, dass unsere zahlreichen Kunden tagtäglich einen maßgeschneiderten Marketinganzug tragen können, der in jeglicher Hinsicht überzeugen kann.</p>
    <p>Damit Sie nicht „von der Stange“ kaufen müssen, bieten wir Ihnen eine individuelle und nur auf Ihre Bedürfnisse abgestimmte Lösung an. Somit erhalten Sie die gesamte Marketing-Palette zeitsparend aus einer Hand.</p>
    <p>Lassen Sie uns gemeinsam über Ihre Ziele und Wünsche sprechen. In einem unverbindlichen und selbstverständlich kostenfreien Erstgespräch erörtern wir detailliert und zielgenau die passende Strategie für Sie.</p>
  </div>
  <div class="abs about-photo" role="img" aria-label="Videoschnitt am Bildschirm, ein Cutter blickt auf die Timeline"></div>
</section>

<section>
  <h2 class="abs script section-title" style="top:1376px">Unsere Leistungen</h2>

  <div class="abs card" style="left:87px;top:1458px">
    <div class="card-photo" role="img" aria-label="Fernsehzeitschrift neben einer orangefarbenen Tasse" style="background:linear-gradient(135deg,#e07a1e,#c8323a 50%,#2b2b2b)"></div>
    <div class="card-label"><svg width="20" height="12" viewBox="0 0 20 12" fill="none" stroke="#fff" stroke-width="1"><path d="M0 6h18M12 1l6 5-6 5"/></svg>Print</div>
  </div>
  <div class="abs card" style="left:432px;top:1458px">
    <div class="card-photo" role="img" aria-label="Interview vor der Kamera auf einer Messe" style="background:linear-gradient(135deg,#6f9ccc,#4d5a68 50%,#2a2a2a)"></div>
    <div class="card-label"><svg width="20" height="12" viewBox="0 0 20 12" fill="none" stroke="#fff" stroke-width="1"><path d="M0 6h18M12 1l6 5-6 5"/></svg>TV &amp; Radio</div>
  </div>
  <div class="abs card" style="left:777px;top:1458px">
    <div class="card-photo" role="img" aria-label="Konferenzraum mit Präsentation am Bildschirm" style="background:linear-gradient(135deg,#5d5f63,#8a7a63 55%,#2e2e30)"></div>
    <div class="card-label"><svg width="20" height="12" viewBox="0 0 20 12" fill="none" stroke="#fff" stroke-width="1"><path d="M0 6h18M12 1l6 5-6 5"/></svg>Internet (Digital) und Events</div>
  </div>
  <div class="abs card" style="left:87px;top:1750px">
    <div class="card-photo" role="img" aria-label="Preisverleihung auf einer Bühne mit Rednerpult" style="background:linear-gradient(135deg,#4a2a6a,#a04a5a 50%,#1f1f2a)"></div>
    <div class="card-label"><svg width="20" height="12" viewBox="0 0 20 12" fill="none" stroke="#fff" stroke-width="1"><path d="M0 6h18M12 1l6 5-6 5"/></svg>Kommunikation- und<br>Marketingkonzepte</div>
  </div>
  <div class="abs card" style="left:432px;top:1750px">
    <div class="card-photo" role="img" aria-label="Koch bei der Zubereitung auf einem Event" style="background:linear-gradient(135deg,#7a5a3a,#c9b9a4 50%,#2e2a26)"></div>
    <div class="card-label"><svg width="20" height="12" viewBox="0 0 20 12" fill="none" stroke="#fff" stroke-width="1"><path d="M0 6h18M12 1l6 5-6 5"/></svg>Realisierung von Events</div>
  </div>
  <div class="abs card" style="left:777px;top:1750px">
    <div class="card-photo" role="img" aria-label="Moderatoren im hellen TV-Studio" style="background:linear-gradient(135deg,#e8eef0,#9fb5bc 50%,#3a3f44)"></div>
    <div class="card-label"><svg width="20" height="12" viewBox="0 0 20 12" fill="none" stroke="#fff" stroke-width="1"><path d="M0 6h18M12 1l6 5-6 5"/></svg>TV-Produktion</div>
  </div>
</section>

<section>
  <div class="abs cta"></div>
  <h2 class="abs script cta-title">Jetzt Individuell beraten lassen</h2>
  <div class="abs cta-text">Möchten Sie in Ruhe über Ihr Projekt sprechen?<br>Kein Problem – unsere Kolleginnen und Kollegen nehmen sich gerne Zeit für Sie!</div>
  <a class="abs btn" style="left:709px;top:2222px;width:231px;height:37px;border-radius:19px">Jetzt Kontakt aufnehmen</a>
</section>

<footer>
  <div class="abs foot-col" style="left:87px"><h4>Agentur</h4><ul><li>Team</li><li>Karriere bei Uns</li><li>Häufig gestellte Fragen</li></ul></div>
  <div class="abs foot-col" style="left:346px"><h4>Leistungen</h4><ul><li>Print</li><li>TV</li><li>Radio</li><li>Internet &amp; Events</li><li>Kommunikation- und Marketingkonzepte</li><li>Events und TV-Produktionen</li></ul></div>
  <div class="abs foot-col" style="left:605px"><h4>Service</h4><ul><li>Kontakt</li><li>Projektmanagement</li></ul></div>
  <div class="abs foot-col" style="left:864px"><h4>Freundeskreis</h4><ul><li>Impressum</li><li>Datenschutzerklärung</li><li>Cookies</li></ul></div>
  <div class="abs made">MADE WITH
    <svg width="16" height="14" viewBox="0 0 16 14" fill="none" stroke="var(--accent)" stroke-width="1.6"><path d="M8 13S1 8.5 1 4.5A3.5 3.5 0 0 1 8 3a3.5 3.5 0 0 1 7 1.5C15 8.5 8 13 8 13z"/></svg>
  </div>
</footer>

</body>
</html>
```